Cover Page for Financial Statements

We need a cover page designed for our Financial Statements. It will need to include our business logo and the Chartered accountant logo.
We have included our current title page ( image titled full.png ) to show all the information that is needed to be included such as the title 'Financial Statements' and 'The year ended March 2023'. We would like to see designs that reflect our logo but also adds some interest with objects / deisngs that fill up more of the page.

Industry/Entity Type

Accounting

Font styles to use
Serif
Sans Serif

Colors

Designer to choose only greyscale colors for use in the design.

Requirements
Must have
• - A4 document size, our logo, Chartered Accountant Logo
Should not have
• Bright Colors

```html
<!DOCTYPE html>
<html lang="en">
<head>
<meta charset="utf-8">
<title>Financial Statements Cover – Keel Ledger</title>
<link href="https://fonts.googleapis.com/css2?family=Inter:wght@400;500;700&display=swap" rel="stylesheet">
<style>
  :root {
    --backdrop: #efefef;
    --paper: #ffffff;
    --ink: #000000;
    --badge-grey: #8a8a8a;
  }
  html, body {
    margin: 0;
    padding: 0;
    width: 1200px;
    height: 900px;
    overflow: hidden;
    background: var(--backdrop);
  }
  .cover-page {
    position: absolute;
    left: 305px;
    top: 40px;
    width: 590px;
    height: 820px;
    display: block;
    box-shadow: 0 2px 10px rgba(0,0,0,0.12);
  }
  .paper { fill: var(--paper); }
  .ink-field { fill: var(--ink); }
  .rule { fill: var(--paper); }
  .badge { fill: var(--badge-grey); }
  .brand-name {
    font-family: "Inter", sans-serif;
    font-weight: 500;
    font-size: 27px;
    letter-spacing: 3px;
    fill: var(--ink);
  }
  .title {
    font-family: "Inter", sans-serif;
    font-weight: 700;
    font-size: 61px;
    letter-spacing: 1.5px;
    fill: var(--paper);
  }
  .period-label {
    font-family: "Inter", sans-serif;
    font-weight: 400;
    font-size: 24px;
    fill: var(--paper);
  }
  .period-date {
    font-family: "Inter", sans-serif;
    font-weight: 700;
    font-size: 68px;
    letter-spacing: 1px;
    fill: var(--paper);
  }
</style>
</head>
<body>
  <svg class="cover-page" viewBox="0 0 590 820" xmlns="http://www.w3.org/2000/svg">
    <!-- page base -->
    <rect class="paper" x="0" y="0" width="590" height="820"/>
    <rect class="ink-field" x="0" y="100" width="590" height="720"/>

    <!-- header: professional body badge and firm name -->
    <rect class="badge" x="78" y="30" width="34" height="34"/>
    <rect class="paper" x="277" y="90" width="260" height="53"/>
    <text class="brand-name" x="407" y="88" text-anchor="middle">KEEL LEDGER</text>

    <!-- upper accents -->
    <rect class="rule" x="60" y="208" width="34" height="34"/>
    <rect class="rule" x="277" y="208" width="257" height="7"/>
    <rect class="rule" x="527" y="208" width="7" height="127"/>

    <!-- title -->
    <text class="title" x="55" y="323">FINANCIAL</text>
    <text class="title" x="55" y="387">STATEMENTS</text>

    <!-- lower bracket and bar -->
    <rect class="rule" x="56" y="430" width="7" height="182"/>
    <rect class="rule" x="56" y="605" width="194" height="7"/>
    <rect class="rule" x="269" y="490" width="321" height="13"/>

    <!-- reporting period -->
    <text class="period-label" x="273" y="543">FOR THE YEAR ENDED</text>
    <text class="period-date" x="270" y="608">MARCH</text>
    <text class="period-date" x="270" y="681">2023</text>

    <!-- stepped corner -->
    <rect class="paper" x="540" y="690" width="50" height="130"/>
    <rect class="paper" x="454" y="772" width="136" height="48"/>
  </svg>
</body>
</html>
```